Design ecommerce website for www.velmorissa.com

Design a Website given below details
Name - www.velmorissa.com

Given a shopify theme :Brightcart
http://layoutbazaar.net/item/brightcart-responsive-shopify-theme/4817203

Given type of products that will be sold
http://tarokbars.pelisite.com
Wendlomart.in
( above designs are not good )

Given competitors
www.zorbelle.com ( especially like how each category is sold as a story )
www.gindova.com

Given Tg
Women 20 +
Aspirational

Website has to be fresh peppy and understated sexy

No need to push Organic agenda too much but it is present in background story

Let me know if any more info required
Updates

Reason: Look for forward to revised designs / new designs

Target Market(s)

Women
20 +
Primarily Indian
Aspirational

Industry/Entity Type

Hair And Beauty

Number of Pages Required

5+ page

Font styles to use
Sans Serif

Requirements
Must have
• Hi Quality Images ( i will provide images )
• Good fun icons
• Good font
• Peppy / classy color scheme
• THe main focus is on the main page / landing page. Need a design which is intuitive and lends itself well to beauty products. Creating an exclusive experiance for women
• The other pages are
• Modified page for product categories ( eg page for all Skin products )
• Modified page for each product
• About page / Check out page
• These are essentially modifications to main page with minor alterations
• Important to remember that we are building using the Brightcart Shopify theme.
• If you recommend shopify apps, I would purchase those too.
Nice to have
• Disctintive fonts.
• Usage of elements/ fonts / icons which make the site very quirky and fun
• I am open to suggestions to changes in words or using images instead of words to convey information
Should not have
• Too much of green / organic feel
• Too much artificial feel ( no neons )

```html
<!DOCTYPE html>
<html lang="en">
<head>
<meta charset="utf-8">
<title>velmorissa — beauty store</title>
<link href="https://fonts.googleapis.com/css2?family=Open+Sans:wght@300;400;600;700&display=swap" rel="stylesheet">
<style>
:root{
  --blue:#1f6fc4;
  --brand:#6aa52c;
  --ink:#333;
  --muted:#888;
  --line:#e2e2e2;
  --soft:#f3f3f3;
  --night:#0b0b0b;
  --teal-a:#4b8792;
  --teal-b:#0f2e37;
  --white:#fff;
}
*{box-sizing:border-box;margin:0;padding:0}
html,body{width:691px;height:1200px;overflow:hidden;background:var(--white)}
body{font-family:"Open Sans",Arial,sans-serif;color:var(--ink);font-size:7px;line-height:1.4}
.wrap{width:576px;margin:0 auto;position:relative}
a{color:inherit;text-decoration:none}

/* header */
.site-header{height:76px;position:relative}
.promo-strip{position:absolute;right:62px;top:0;width:300px;height:20px;background:#f1eee9;display:flex;align-items:center;justify-content:center;gap:10px;font-size:8px}
.promo-brand{color:var(--brand);font-weight:600}
.promo-deal{font-weight:700;letter-spacing:.5px}
.promo-btn{background:var(--ink);color:var(--white);font-size:5px;padding:2px 5px}
.logo{position:absolute;left:57px;top:32px;display:flex;align-items:center;gap:5px;color:var(--brand);font-size:18px;font-weight:600;letter-spacing:-.3px}
.logo-dot{width:7px;height:7px;border-radius:50%;background:var(--brand)}
.header-links{position:absolute;right:57px;top:40px;display:flex;align-items:center;gap:14px;font-size:6px;color:#555}
.header-links span{display:flex;align-items:center;gap:3px}
.header-search{width:60px;height:11px;border:1px solid var(--line);font-size:5.5px;color:#aaa;padding:1px 3px}

/* nav */
.main-nav{height:18px;background:var(--blue)}
.main-nav ul{list-style:none;display:flex;height:18px;align-items:center}
.main-nav li{color:var(--white);font-size:6px;padding:0 15px;height:18px;line-height:18px}
.main-nav li.active{background:var(--white);color:var(--blue);margin:3px 6px 0 0;height:15px;line-height:15px;padding:0 14px}

/* hero */
.hero{height:180px;position:relative;background:linear-gradient(100deg,var(--teal-a) 0,#2d5f69 45%,var(--teal-b) 100%);overflow:hidden}
.hero-photo{position:absolute;left:150px;top:0;width:250px;height:180px;
  background:
    radial-gradient(ellipse 34% 40% at 52% 52%,#f0d2bf 0,#e2b59c 60%,rgba(226,181,156,0) 100%),
    linear-gradient(160deg,#e0703c 0,#c24a25 35%,#8f2f18 60%,rgba(60,100,110,0) 92%);
  border-radius:0 0 40% 0}
.hero-copy{position:absolute;left:410px;top:48px;width:170px;text-align:center;color:var(--white)}
.hero-kicker{font-size:7px;letter-spacing:2px;font-weight:600}
.hero-title{font-size:22px;font-weight:300;line-height:1.25}
.hero-offer{font-size:9px;letter-spacing:2px}
.hero-btn{display:inline-block;margin-top:10px;border:1px solid var(--white);font-size:5.5px;padding:4px 10px;letter-spacing:1px}
.hero-arrow{position:absolute;top:80px;width:12px;height:20px}
.hero-arrow.prev{left:62px}.hero-arrow.next{right:62px}
.hero-dots{position:absolute;bottom:8px;left:0;right:0;display:flex;justify-content:center;gap:4px}
.hero-dots i{width:4px;height:4px;border-radius:50%;background:rgba(255,255,255,.5)}
.hero-dots i:first-child{background:var(--white)}

/* signup line */
.signup-line{height:30px;line-height:30px;text-align:center;font-size:6px;color:#555}
.signup-line b{color:var(--blue)}

/* category cards */
.categories{margin-top:10px;height:124px;display:flex;justify-content:space-between}
.category-card{width:137px;height:124px;border:1px solid var(--line);box-shadow:0 1px 4px rgba(0,0,0,.1);position:relative;padding:4px;background:var(--white)}
.category-img{height:100%}
.cat-1 .category-img{background:linear-gradient(150deg,#f4f0ea 0,#e4d3bd 45%,#b89471 100%)}
.cat-2 .category-img{background:linear-gradient(150deg,#e7e4e6 0,#c9a99a 50%,#7b5f56 100%)}
.cat-3 .category-img{background:linear-gradient(150deg,#f0f5f7 0,#d9c2b4 55%,#a8c2cc 100%)}
.cat-4 .category-img{background:linear-gradient(150deg,#f7f0d8 0,#e2c067 50%,#a8782a 100%)}
.category-btn{position:absolute;left:50%;transform:translateX(-50%);bottom:16px;background:var(--blue);color:var(--white);font-size:5.5px;padding:3px 8px;white-space:nowrap}

/* game band */
.game-band{margin-top:34px;height:130px;background:var(--night);position:relative;overflow:hidden}
.game-photo{position:absolute;left:70px;top:0;width:180px;height:130px;
  background:radial-gradient(ellipse 30% 40% at 58% 55%,#c99a7e 0,#8a5d45 55%,rgba(40,28,22,0) 100%),
             linear-gradient(90deg,#0b0b0b 0,#2a1d16 40%,#1a120e 70%,#0b0b0b 100%)}
.game-copy{position:absolute;left:270px;top:40px;color:var(--white)}
.game-title{font-size:16px;font-weight:300}
.game-sub{font-size:5.5px;color:#aaa;margin-top:2px}
.game-btn{display:inline-block;margin-top:9px;border:1px solid #888;font-size:5.5px;padding:3px 9px}

/* products */
.section-band{margin-top:12px;height:16px;background:var(--blue);color:var(--white);text-align:center;font-size:6px;line-height:16px}
.products{height:150px;display:flex;justify-content:space-between;padding-top:14px}
.product{width:184px;position:relative;padding:0 8px}
.product + .product{border-left:1px solid var(--line)}
.product-img{height:86px;margin:0 30px;border-radius:3px}
.p1 .product-img{background:radial-gradient(ellipse 22% 50% at 50% 50%,#c7a47c 0,#9c7a54 60%,rgba(255,255,255,0) 100%),#f8f5f1}
.p2 .product-img{background:radial-gradient(ellipse 30% 48% at 50% 50%,#c82626 0,#7a1010 60%,rgba(255,255,255,0) 100%),#f8f4f4}
.p3 .product-img{background:radial-gradient(ellipse 40% 48% at 50% 50%,#3a3530 0,#c98f2c 55%,rgba(255,255,255,0) 100%),#f8f6f1}
.product-name{font-size:5.5px;color:#555;margin-top:10px}
.product-price{font-size:5.5px;color:var(--muted)}
.product-price s{margin-right:4px}
.product-price b{color:var(--blue);font-weight:600}
.product-add{position:absolute;right:8px;bottom:16px;width:11px;height:11px;background:var(--brand)}
.p2 .product-add{background:var(--blue)}
.p3 .product-add{background:#d33}

/* testimonial */
.testimonial{height:80px;text-align:center;padding:20px 70px 0;font-size:5.5px;color:var(--muted)}
.testimonial a{display:block;color:var(--blue);margin-top:4px}
.testimonial .dots{display:flex;justify-content:center;gap:3px;margin-top:4px}
.testimonial .dots i{width:3px;height:3px;border-radius:50%;background:#ccc}
.testimonial .dots i:first-child{background:var(--blue)}

/* info row */
.info-row{height:100px;border-top:1px solid var(--line);display:flex;gap:24px;padding-top:22px}
.info-col h4{font-size:6px;font-weight:600;color:#444;margin-bottom:5px}
.info-subscribe{width:210px}
.subscribe-form{display:flex}
.subscribe-input{flex:1;height:12px;border:1px solid var(--line);font-size:5px;color:#aaa;padding:2px 3px}
.subscribe-btn{width:18px;height:12px;background:var(--blue)}
.info-about{width:220px;font-size:5.5px;color:var(--muted)}
.info-about a{color:var(--blue)}
.info-social{margin-left:auto}
.social{display:flex;gap:4px}
.social i{width:11px;height:11px;border-radius:50%;background:#9a9a9a}

/* footer columns */
.footer-cols{height:130px;border-top:1px solid var(--line);display:flex;justify-content:space-between;padding-top:22px}
.footer-col h5{font-size:6px;font-weight:600;color:#444;margin-bottom:6px}
.footer-col li{list-style:none;font-size:5.5px;color:var(--muted);line-height:1.8}
.footer-phone{font-size:12px;color:var(--blue);font-weight:600;margin-top:2px}
.pay-cards{display:flex;gap:3px;margin-top:2px}
.pay-cards i{width:18px;height:12px;border-radius:2px}
.pay-cards i:nth-child(1){background:#1a3d8f}
.pay-cards i:nth-child(2){background:#e0a02a}
.pay-cards i:nth-child(3){background:#2a8fd6}

/* features */
.features{height:70px;background:var(--soft)}
.features .wrap{display:flex;justify-content:space-around;padding-top:16px}
.feature{text-align:center;width:140px}
.feature svg{display:block;margin:0 auto 3px}
.feature h6{font-size:6px;font-weight:600;color:#555}
.feature p{font-size:5px;color:var(--muted)}

/* bottom */
.bottom-bar{height:40px;text-align:center;padding-top:11px;font-size:5px;color:var(--muted);background:#fafafa;border-top:1px solid var(--line)}
.bottom-bar p + p{margin-top:3px}
</style>
</head>
<body>

<header class="site-header">
  <div class="promo-strip">
    <span class="promo-brand">velmorissa</span>
    <span class="promo-deal">FLAT 15% OFF</span>
    <span class="promo-btn">SHOP NOW</span>
  </div>
  <a class="logo" href="#"><span class="logo-dot"></span>velmorissa</a>
  <div class="header-links">
    <span><svg width="6" height="6" viewBox="0 0 10 10"><circle cx="4" cy="4" r="3" fill="none" stroke="#777" stroke-width="1.5"/><path d="M6 6l3 3" stroke="#777" stroke-width="1.5"/></svg>Search</span>
    <span><svg width="6" height="6" viewBox="0 0 10 10"><circle cx="5" cy="3" r="2.4" fill="#777"/><path d="M1 10c0-3 8-3 8 0z" fill="#777"/></svg>My Account</span>
    <span><svg width="6" height="6" viewBox="0 0 10 10"><path d="M1 3h8l-1 7H2z" fill="#777"/></svg>Shopping Bag</span>
    <span class="header-search">search</span>
  </div>
</header>

<nav class="main-nav">
  <ul class="wrap">
    <li class="active">Skin</li>
    <li>Hair</li>
    <li>Make Up</li>
    <li>Bath &amp; Body</li>
  </ul>
</nav>

<section class="hero">
  <div class="hero-photo" role="img" aria-label="Portrait photo of a woman with flowing red hair"></div>
  <svg class="hero-arrow prev" viewBox="0 0 12 20"><path d="M9 3L3 10l6 7" fill="none" stroke="#fff" stroke-width="1.5"/></svg>
  <svg class="hero-arrow next" viewBox="0 0 12 20"><path d="M3 3l6 7-6 7" fill="none" stroke="#fff" stroke-width="1.5"/></svg>
  <div class="hero-copy">
    <p class="hero-kicker">ENHANCE YOUR BEAUTY</p>
    <p class="hero-title">velmorissa</p>
    <p class="hero-offer">FLAT 15% OFF</p>
    <a class="hero-btn" href="#">REGISTER NOW</a>
  </div>
  <div class="hero-dots"><i></i><i></i><i></i><i></i><i></i></div>
</section>

<p class="signup-line">Catch the Season's Best Recommendations, Trial packs, Offers, and personalised wishes. <b>SIGN UP</b></p>

<section class="categories wrap">
  <div class="category-card cat-1"><div class="category-img" role="img" aria-label="Photo of a wrapped beauty gift set"></div><span class="category-btn">buy Gift Set</span></div>
  <div class="category-card cat-2"><div class="category-img" role="img" aria-label="Photo of a woman in soft light"></div><span class="category-btn">natural beauty secrets</span></div>
  <div class="category-card cat-3"><div class="category-img" role="img" aria-label="Photo of hands applying skin cream"></div><span class="category-btn">skin care essentials</span></div>
  <div class="category-card cat-4"><div class="category-img" role="img" aria-label="Photo of oil bottles and flowers"></div><span class="category-btn">hair care rituals</span></div>
</section>

<section class="game-band">
  <div class="game-photo" role="img" aria-label="Photo of a woman with sleek dark hair"></div>
  <div class="game-copy">
    <p class="game-title">play the natural beauty game</p>
    <p class="game-sub">discover looks made for you and win exclusive rewards</p>
    <a class="game-btn" href="#">discover now</a>
  </div>
</section>

<div class="section-band">velmorissa nice</div>

<section class="products wrap">
  <div class="product p1">
    <div class="product-img" role="img" aria-label="Product photo of a foundation bottle"></div>
    <p class="product-name">Velvet Glow Foundation</p>
    <p class="product-price"><s>₹249.00</s><b>₹199.00</b></p>
    <span class="product-add"></span>
  </div>
  <div class="product p2">
    <div class="product-img" role="img" aria-label="Product photo of a lip tint box"></div>
    <p class="product-name">Rose Lip Tint</p>
    <p class="product-price"><s>₹249.00</s><b>₹199.00</b></p>
    <span class="product-add"></span>
  </div>
  <div class="product p3">
    <div class="product-img" role="img" aria-label="Product photo of two face cream tubes"></div>
    <p class="product-name">Hydra Face Cream Duo</p>
    <p class="product-price"><s>₹249.00</s><b>₹199.00</b></p>
    <span class="product-add"></span>
  </div>
</section>

<section class="testimonial wrap">
  <p>Loved the gentle textures and the soft fragrance. My skin feels fresh all day and the delivery was quick. The trial pack made it easy to find my shade. Truly a treat for every morning.</p>
  <a href="#">view more</a>
  <div class="dots"><i></i><i></i><i></i></div>
</section>

<section class="info-row wrap">
  <div class="info-col info-subscribe">
    <h4>subscribe special discounts on your inbox</h4>
    <div class="subscribe-form"><span class="subscribe-input">Enter your email</span><span class="subscribe-btn"></span></div>
  </div>
  <div class="info-col info-about">
    <h4>about velmorissa</h4>
    <p>Beauty essentials crafted with care, inspired by nature and made for the modern woman who loves to feel good. <a href="#">read more</a></p>
  </div>
  <div class="info-col info-social">
    <h4>quick social</h4>
    <div class="social"><i></i><i></i><i></i><i></i></div>
  </div>
</section>

<footer>
  <div class="footer-cols wrap">
    <div class="footer-col"><h5>shop by brand</h5><ul><li>Skin Care</li><li>Hair Care</li><li>Make Up</li><li>Bath &amp; Body</li></ul></div>
    <div class="footer-col"><h5>company profile</h5><ul><li>About Us</li><li>Our Story</li><li>Careers</li><li>Press</li></ul></div>
    <div class="footer-col"><h5>customer info</h5><ul><li>Track Order</li><li>Returns</li><li>Shipping</li><li>FAQs</li></ul></div>
    <div class="footer-col"><h5>24x7 services</h5><ul><li>Call us anytime</li></ul><p class="footer-phone">40 2718 9365</p></div>
    <div class="footer-col"><h5>payment options</h5><div class="pay-cards"><i></i><i></i><i></i></div></div>
  </div>

  <section class="features">
    <div class="wrap">
      <div class="feature">
        <svg width="18" height="14" viewBox="0 0 18 14"><path d="M1 2h10v8H1zM11 5h4l2 3v2h-6z" fill="none" stroke="#777" stroke-width="1"/><circle cx="4" cy="11.5" r="1.5" fill="#777"/><circle cx="14" cy="11.5" r="1.5" fill="#777"/></svg>
        <h6>free delivery</h6><p>on all orders above ₹499</p>
      </div>
      <div class="feature">
        <svg width="16" height="14" viewBox="0 0 16 14"><path d="M2 4l6-3 6 3v7l-6 3-6-3z M2 4l6 3 6-3 M8 7v7" fill="none" stroke="#777" stroke-width="1"/></svg>
        <h6>special shipment</h6><p>packed with love and care</p>
      </div>
      <div class="feature">
        <svg width="16" height="14" viewBox="0 0 16 14"><path d="M3 7a5 5 0 1 0 2-4" fill="none" stroke="#777" stroke-width="1.2"/><path d="M2 1v4h4" fill="none" stroke="#777" stroke-width="1.2"/></svg>
        <h6>free returns</h6><p>easy returns within 15 days</p>
      </div>
    </div>
  </section>

  <div class="bottom-bar">
    <p>privacy policy | terms &amp; conditions | return policy</p>
    <p>© 2024 velmorissa. All rights reserved.</p>
  </div>
</footer>

</body>
</html>
```